Bright tap water company advertisment

We want to design a 1/3 page A4 mini ad for a magazine AND a full a4 page brochure that will be an email attachment. The mini ad can be a simpler version of the A4.

The company is Bright Tap Flow, we sell Thermolia heat pumps and Raydeck solar hot water units.

I have attached a copy of the brochure of the units we sell as well as the logo and a few screen shots of our website that is not quite finished, our pantone colours are forest, basil and grass.

Our slogan is 'maximum heat, Minimum impact'

and then a picture of a heat pump and a picture of a solar hot water unit somewhere.
it needs to say the following:
Start your journey today towards a greener tomorrow with Raydeck or Thermolia
Up to 71% more economical than traditional units
Rebates up to $2000 may apply
contact 1300 47 61 52 for details
Brighttapflow.com.au

Raydeck Solar Hot Water
 Tanks manufactured in Australia and Holland
 Copper collectors which are the most efficient on the market
 Circulation Pump manufactured in Europe
 All standard installation parts included – no hidden costs
 Standard Solar Thermostat & 2.4kw Element (available at any plumbing supplier)
 Warranty – 7 year tank and panel

Thermolia Heat Pump
 Draw 0.6kw of power
 Require only a standard weather proof power point
 Has a back up element.
 Dual anodes for extra corrosion resistance.
 Warranty – 5 year tank, 3 years refrigerant components

Target Market(s)

the public

Industry/Entity Type

plumbing

Font styles to use
Sans Serif

Requirements
Must have
• simplicity and creativity

```html
<!DOCTYPE html>
<html lang="en">
<head>
<meta charset="utf-8">
<title>Bright Tap Flow – Maximum Heat, Minimum Impact</title>
<link rel="stylesheet" href="https://fonts.googleapis.com/css2?family=Poppins:wght@400;500;600;700;800;900&display=swap">
<style>
  :root {
    --forest: #1b4a2a;
    --basil: #2f8f45;
    --grass: #3fae55;
    --mint: #a3cea6;
    --ink: #1f2a22;
    --stage: #e8e8e9;
    --photo-dark: #6f6f72;
    --photo-light: #b9b9bb;
  }
  * { margin: 0; padding: 0; box-sizing: border-box; }
  html, body {
    width: 720px; height: 1200px; overflow: hidden;
    background: var(--stage);
    font-family: "Poppins", sans-serif;
  }
  .brochure {
    position: absolute; left: 10px; top: 105px;
    width: 700px; height: 990px; overflow: hidden;
    background: #fff;
    box-shadow: 0 4px 14px rgba(0,0,0,.25);
  }
  .brochure-art { position: absolute; inset: 0; }
  .bathroom-photo {
    position: absolute; inset: 0;
    clip-path: path("M0,262 C180,165 420,105 700,102 L700,385 C400,380 150,430 0,534 Z");
    background: linear-gradient(135deg, var(--photo-dark) 0%, #8c8c8f 55%, var(--photo-light) 100%);
  }
  .brand {
    position: absolute; left: 11px; top: 20px; width: 180px;
    text-align: center; color: var(--basil);
    font-weight: 600; font-size: 25px; line-height: 27px;
  }
  .brand-mark {
    display: block; width: 58px; height: 58px; margin: 0 auto 16px;
    border-radius: 50%; background: var(--basil);
  }
  .slogan {
    position: absolute; left: 32px; top: 215px; width: 260px;
    text-align: center; color: var(--forest); font-weight: 800;
  }
  .slogan .small { display: block; font-size: 28px; line-height: 34px; }
  .slogan .large { display: block; font-size: 58px; line-height: 62px; letter-spacing: 1px; }
  .product { position: absolute; }
  .product-heatpump {
    left: 470px; top: 247px; width: 138px; height: 494px;
    background: linear-gradient(90deg, #c9c9c7 0%, #efefed 40%, #bdbdbb 100%);
  }
  .product-solar {
    left: 57px; top: 425px; width: 320px; height: 316px;
    background: linear-gradient(90deg, #ecebe5 0%, #ecebe5 38%, #4a5753 42%, #8c9893 80%, #dfe2de 100%);
  }
  .product-name {
    position: absolute; color: var(--ink); font-weight: 500;
  }
  .product-heatpump .product-name {
    left: 50px; top: 30px; font-size: 16px;
    writing-mode: vertical-rl;
  }
  .product-solar .product-name { left: 40px; top: 6px; font-size: 10px; }
  .contact {
    position: absolute; left: 23px; top: 750px; width: 360px;
    text-align: center; color: var(--ink);
  }
  .contact-heading { font-size: 17px; font-weight: 600; line-height: 28px; }
  .contact-body { font-size: 17px; font-weight: 500; line-height: 28px; letter-spacing: .3px; }
  .contact-phone { margin-top: 6px; font-size: 26px; font-weight: 700; color: var(--forest); line-height: 34px; }
  .contact-phone span { font-size: 19px; font-weight: 500; color: var(--ink); }
  .contact-web { font-size: 26px; font-weight: 600; color: var(--forest); line-height: 34px; letter-spacing: .3px; }
  .offer {
    position: absolute; left: 426px; top: 776px; width: 250px;
    text-align: center; color: var(--forest);
  }
  .offer-rebate { font-size: 16px; font-weight: 500; line-height: 21px; }
  .offer-rebate b { font-weight: 800; font-size: 18px; }
  .offer-saving { margin-top: 14px; font-size: 16px; font-weight: 500; line-height: 23px; }
  .offer-saving .figure { font-size: 44px; font-weight: 800; line-height: 40px; vertical-align: -6px; }
  .offer-saving b { font-size: 22px; font-weight: 800; }
  .offer-saving .strong { font-weight: 700; font-size: 17px; }
</style>
</head>
<body>
<main class="brochure">
  <svg class="brochure-art" viewBox="0 0 700 990" width="700" height="990" aria-hidden="true">
    <defs>
      <linearGradient id="paper" x1="0" y1="0" x2="1" y2="0">
        <stop offset="0" stop-color="#d9d9da"/><stop offset=".22" stop-color="#fff"/>
        <stop offset=".8" stop-color="#fff"/><stop offset="1" stop-color="#dcdcdd"/>
      </linearGradient>
    </defs>
    <rect class="paper" width="700" height="990" fill="url(#paper)"/>
  </svg>

  <div class="bathroom-photo" role="img" aria-label="Photo of a grey tiled bathroom with a rain shower head running"></div>

  <svg class="brochure-art" viewBox="0 0 700 990" width="700" height="990" aria-hidden="true">
    <path class="band-top" d="M0,256 C180,160 420,100 700,97 L700,104 C420,108 180,168 0,264 Z" fill="var(--basil)"/>
    <circle class="offer-disc" cx="605" cy="866" r="212" fill="var(--mint)" stroke="#fff" stroke-width="4"/>
    <rect class="rule-thick" x="0" y="976" width="700" height="4" fill="var(--basil)"/>
    <rect class="rule-thin" x="0" y="983" width="700" height="3" fill="var(--grass)"/>
  </svg>

  <div class="brand"><span class="brand-mark"></span>Bright Tap<br>Flow</div>

  <div class="product product-solar" role="img" aria-label="Photo of a Raydeck solar hot water tank beside a rooftop solar collector panel"><span class="product-name">Raydeck</span></div>
  <div class="product product-heatpump" role="img" aria-label="Photo of a Thermolia heat pump water heater"><span class="product-name">Thermolia</span></div>

  <h1 class="slogan">
    <span class="small">MAXIMUM</span>
    <span class="large">HEAT,</span>
    <span class="small">MINIMUM</span>
    <span class="large">IMPACT</span>
  </h1>

  <section class="contact">
    <p class="contact-heading">Contact us</p>
    <p class="contact-body">Today to start your journey<br>towards a greener tomorrow Cal us</p>
    <p class="contact-phone">1300 47 61 52 <span>or go to</span></p>
    <p class="contact-web">brighttapflow.com.au</p>
  </section>

  <section class="offer">
    <p class="offer-rebate"><b>STC rebate</b> and <b>REPS subsidy</b> may apply contact us to check your eligibility</p>
    <p class="offer-saving">They are up to <span class="figure">71%</span><br><b>cheaper</b> to run than<br><span class="strong">traditional units</span></p>
  </section>
</main>
</body>
</html>
```